Book Cover (HALF OF ALL WORRIES FADE AWAY)

This book is a series of blog posts from my blog, Notes Fit for Borrowing, which is at glenmarwick.com/blog.
The book is to be called:
HALF OF ALL WORRIES FADE AWAY
And 51 other Notes Fit for Borrowing from the Small Business Sage
(Notes Fit for Borrowing) should be italicized.
My name is Glen Marwick, M.B.A.

I will need three variations for my paperback, hardcover and e-book.
Here are some of the blog titles and their topics:
Preparing Your Small Business For Recession small business recession
Should I Incorporate My Business? Should I Incorporate My Business?
Alternative to Minority Shareholder In Small Private Companies minority shareholder
Small Business Culture – Getting it Right Small Business Culture
What is The Right Way to Fire Someone The Right Way to Fire Someone
The Five Basic Leadership Principles Leadership Principles
10 Tips for New Entrepreneurs – Sure Ways to Increase Your Chances of Success
10 things to consider before becoming an entrepreneur
Strategy vs Biz Plans small business strategy
Closing Sales close the sale
Breakeven break even
Growth makes cash flow suck cash flow issues
Think Twice About Offering Early Payment Discounts prepayment discounts
Firing Customers firing customers
Collections best practices getting paid faster
The Cash Flow Statement cash flow statement
Using Paralegals paralegal
Radical Candor radical candor
Why No is the Second Best Word to a Salesperson's ears value of no
The $8 Million Problem -
Contractor vs Employee contractor vs employee
The Vantrell sales tactic
Systems Turn Goals From Dreams Into Reality Systems vs Goals
The Importance of Realistic Goals stretch goals
Why The Owner Must Review Every Hire hiring for values
Systems Thinking for Small Biz: The Case for SOPs systems thinking
Trust Your Gut business intuition
Grease and friction grease vs friction
Left alone, 90% of problems solve themselves strategic inaction
Referrals Are Great—But Not a Growth Strategy referrals
The Lean Marketing Machine: 7 Hacks to Grow Your Small Business Fast marketing hacks
The Small Business Health Check small business health check
How to Spot a Customer Headed for Trouble — Before They Take You Down With Them customer warning signs
We Are What We Repeatedly Do habits
The Smartest People Know When to Play Dumb playing dumb
Before You Scale, Do the Math unit economics
AI for Small Business: Practical Tools and Use Cases AI for Small Business
Title: Tell Me Right Now—Why Can’t We Raise Your Prices? small business pricing
Why Your Real Competitor Isn’t Who You Think creative destruction
Good Enough Might Be Great satisficing
Bootstrapping: Building Your Business on Your Terms bootstrapping
Building Resilient Companies That Never Have to Bet the Farm bet the farm
We Always Overshoot: From Fiber to Cannabis to AI AI overbuild
A Bias Toward Action bias toward ation
Choosing the Right Business Owner Title business owner title
Jobs to Be Done: Understanding What Your Customers Really Want Jobs to Be Done
Forget Money. Here’s What Really Motivates People. motivation

Target Market(s)

Small business operators, business school students

Industry/Entity Type

Small business

Colors

Designer to choose colors to be used in the design.

Requirements
Should not have
• Should not look cartoonish

```html
<!DOCTYPE html>
<html lang="en">
<head>
<meta charset="utf-8">
<title>Half of All Worries Fade Away — Book Cover Wrap</title>
<link rel="stylesheet" href="https://fonts.googleapis.com/css2?family=Barlow+Condensed:ital,wght@0,500;0,600;0,700;1,500&family=Roboto:wght@400&display=swap">
<style>
  :root {
    --stage: #3e3e3e;
    --paper: #fbfbf5;
    --spine-paper: #f4f4ee;
    --ink: #1d1d1f;
    --body-ink: #2a2a2c;
    --orange-deep: #d8543a;
    --orange-warm: #e6913a;
    --orange-light: #eeae44;
    --blue-deep: #4670b5;
    --blue-mid: #5e93c6;
    --blue-light: #86b8d8;
    --gear-pale: #d6eaf2;
  }
  * { box-sizing: border-box; margin: 0; padding: 0; }
  html, body {
    width: 1200px;
    height: 1200px;
    overflow: hidden;
    background: var(--stage);
  }
  .stage {
    width: 1200px;
    height: 1200px;
    display: flex;
    align-items: center;
    justify-content: center;
  }
  .wrap {
    display: flex;
    height: 780px;
    box-shadow: 0 18px 40px rgba(0,0,0,0.35);
    font-family: "Barlow Condensed", "Arial Narrow", sans-serif;
  }
  .orange-text, .blue-text {
    -webkit-background-clip: text;
    background-clip: text;
    color: transparent;
  }
  .orange-text { background-image: linear-gradient(90deg, var(--orange-deep), var(--orange-warm) 55%, var(--orange-light)); }
  .blue-text { background-image: linear-gradient(90deg, var(--blue-deep), var(--blue-mid) 60%, var(--blue-light)); }

  /* Back cover */
  .back-cover {
    width: 520px;
    height: 780px;
    background: var(--paper);
    padding: 70px 40px 0 44px;
  }
  .back-title {
    text-align: center;
    font-weight: 700;
    font-size: 31px;
    white-space: nowrap;
    letter-spacing: -0.01em;
  }
  .back-subtitle {
    margin-top: 14px;
    text-align: center;
    font-weight: 600;
    font-size: 21px;
    line-height: 1.25;
    color: var(--ink);
  }
  .back-subtitle em { font-style: italic; font-weight: 500; }
  .blurb {
    margin-top: 20px;
    font-family: "Roboto", Arial, sans-serif;
    font-size: 12.5px;
    line-height: 1.78;
    color: var(--body-ink);
    text-align: justify;
  }
  .blurb p + p { margin-top: 20px; }

  /* Spine */
  .spine {
    width: 56px;
    height: 780px;
    background: var(--spine-paper);
    border-left: 1px solid #e2e2da;
    border-right: 1px solid #e2e2da;
    display: flex;
    flex-direction: column;
    align-items: center;
    justify-content: space-between;
    padding: 62px 0 56px;
  }
  .spine-title, .spine-author {
    writing-mode: vertical-rl;
    white-space: nowrap;
  }
  .spine-title {
    font-weight: 700;
    font-size: 25px;
    letter-spacing: 0.02em;
  }
  .spine-title .warm { color: var(--orange-warm); }
  .spine-title .cool { color: var(--blue-mid); }
  .spine-author {
    font-weight: 600;
    font-size: 18px;
    letter-spacing: 0.14em;
    color: var(--ink);
  }

  /* Front cover */
  .front-cover {
    position: relative;
    width: 520px;
    height: 780px;
    background: var(--paper);
    padding: 52px 26px 0 26px;
  }
  .title {
    text-align: center;
    font-weight: 700;
    letter-spacing: -0.01em;
  }
  .title span { display: block; }
  .title-lead { font-size: 50px; line-height: 1; white-space: nowrap; }
  .title-key { font-size: 150px; line-height: 0.9; margin-top: 4px; }
  .title-tail { font-size: 124px; line-height: 0.92; }
  .subtitle {
    margin-top: 14px;
    text-align: right;
    font-weight: 500;
    font-size: 23px;
    line-height: 1.28;
    color: var(--ink);
    padding-right: 14px;
  }
  .subtitle em { font-style: italic; }
  .cover-art {
    position: absolute;
    left: 50px;
    right: 50px;
    top: 480px;
    height: 225px;
    border-radius: 6px;
    background:
      radial-gradient(circle at 22% 22%, rgba(232,132,58,0.5), transparent 32%),
      radial-gradient(circle at 55% 75%, rgba(70,112,181,0.5), transparent 45%),
      linear-gradient(180deg, var(--gear-pale), rgba(134,184,216,0.35) 60%, var(--paper));
  }
  .author {
    position: absolute;
    left: 0;
    right: 0;
    bottom: 28px;
    text-align: center;
    font-weight: 600;
    font-size: 27px;
    letter-spacing: 0.03em;
    color: var(--ink);
  }
</style>
</head>
<body>
  <main class="stage">
    <div class="wrap">
      <section class="back-cover">
        <h2 class="back-title"><span class="orange-text">HALF OF ALL WORRIES</span> <span class="blue-text">FADE AWAY</span></h2>
        <p class="back-subtitle">51 OTHER <em>NOTES FIT FOR BORROWING</em> FROM<br>THE SMALL BUSINESS SAGE</p>
        <div class="blurb">
          <p>Lorem ipsum dolor sit amet, consectetur adipiscing elit, sed do eiusmod tempor incididunt ut labore et dolore magna aliqua. Quis ipsum suspendisse ultrices gravida. Risus commodo viverra maecenas accumsan lacus vel facilisis. Lorem ipsum dolor sit amet, consectetur adipiscing elit, sed do eiusmod tempor incididunt ut labore et dolore magna aliqua. Quis ipsum suspendisse ultrices gravida. Risus commodo viverra maecenas accumsan lacus vel facilisis. Lorem ipsum dolor sit amet, consectetur adipiscing elit, sed do eiusmod tempor incididunt ut labore et dolore magna aliqua.</p>
          <p>Lorem ipsum dolor sit amet, consectetur adipiscing elit, sed do eiusmod tempor incididunt ut labore et dolore magna aliqua. Quis ipsum suspendisse ultrices gravida. Risus commodo viverra maecenas accumsan lacus vel facilisis. Lorem ipsum dolor sit amet, consectetur adipiscing elit, sed do eiusmod tempor incididunt ut labore et dolore magna aliqua. Quis ipsum suspendisse ultrices gravida. Risus commodo viverra maecenas accumsan lacus vel facilisis. Lorem ipsum dolor sit amet, consectetur adipiscing elit, sed do eiusmod tempor incididunt ut labore et dolore magna aliqua.</p>
        </div>
      </section>

      <aside class="spine">
        <p class="spine-title"><span class="warm">HALF OF ALL WORRIES</span> <span class="cool">FADE AWAY</span></p>
        <p class="spine-author">GLEN MARWICK, M.B.A.</p>
      </aside>

      <section class="front-cover">
        <h1 class="title">
          <span class="title-lead orange-text">HALF OF ALL WORRIES</span>
          <span class="title-key blue-text">FADE</span>
          <span class="title-tail blue-text">AWAY</span>
        </h1>
        <p class="subtitle">51 OTHER <em>NOTES FIT FOR BORROWING</em><br>FROM THE SMALL BUSINESS<br>SAGE</p>
        <div class="cover-art" role="img" aria-label="Illustration of interlocking orange, red and pale blue gears above a row of blue silhouetted business people"></div>
        <p class="author">GLEN MARWICK, M.B.A.</p>
      </section>
    </div>
  </main>
</body>
</html>
```